IT Consulting company Needs a Logo Design and Business Cards

I need a New Logo and Business Cards for an established IT Managed Services Company that specializes in flat-rate managed IT services. We provide Design and Build, Help Desk, Onsite and Remote Support Services.

Target Market(s)

Corporate Clients

Industry/Entity Type

It Company

Logo Text

Halbrook Computer Group

Requirements
Nice to have
• Tag Line= Technology at Lightning Speed

```html
<!DOCTYPE html>
<html lang="en">
<head>
<meta charset="utf-8">
<title>Halbrook Computer Group — Business Card</title>
<link rel="stylesheet" href="https://fonts.googleapis.com/css2?family=Roboto:wght@400;500&display=swap">
<style>
  :root {
    --brand-blue: #233a92;
    --brand-blue-text: #1f3894;
    --card-white: #ffffff;
    --ink-grey: #4a4a4a;
    --backdrop: #e6e8ee;
  }
  * { box-sizing: border-box; margin: 0; padding: 0; }
  html, body { width: 1200px; height: 900px; overflow: hidden; }
  body {
    background: var(--backdrop);
    display: flex;
    flex-direction: column;
    align-items: center;
    justify-content: center;
    gap: 50px;
    font-family: "Roboto", Arial, sans-serif;
  }
  .card {
    width: 630px;
    height: 360px;
    border-radius: 22px;
    box-shadow: 0 10px 28px rgba(20, 30, 60, 0.18);
    position: relative;
    display: flex;
    align-items: center;
  }
  .card-front { background: var(--card-white); padding: 0 36px 0 48px; }
  .card-back { background: var(--brand-blue); justify-content: center; }

  .company-name {
    font-family: "Roboto", Arial, sans-serif;
    font-weight: 500;
    color: var(--brand-blue-text);
    font-size: 23px;
    white-space: nowrap;
  }
  .card-back .company-name { color: var(--card-white); font-size: 34px; }

  .divider {
    width: 2px;
    height: 140px;
    background: var(--brand-blue-text);
    margin: 0 30px 0 32px;
    flex-shrink: 0;
  }
  .contact { display: flex; flex-direction: column; white-space: nowrap; }
  .contact-name {
    font-weight: 500;
    color: var(--brand-blue-text);
    font-size: 20px;
    text-transform: uppercase;
  }
  .contact-role { color: var(--ink-grey); font-size: 15px; margin: 2px 0 10px; }
  .contact-list { list-style: none; }
  .contact-item {
    display: flex;
    align-items: center;
    gap: 8px;
    color: var(--ink-grey);
    font-size: 15px;
    line-height: 1.55;
  }
  .contact-icon { width: 13px; height: 13px; flex-shrink: 0; }
</style>
</head>
<body>
  <section class="card card-front">
    <span class="company-name">Halbrook Computer Group</span>
    <div class="divider"></div>
    <div class="contact">
      <span class="contact-name">Daniela Reyes</span>
      <span class="contact-role">Director</span>
      <ul class="contact-list">
        <li class="contact-item">
          <svg class="contact-icon" viewBox="0 0 16 16" aria-hidden="true"><path d="M4 1.5 6 5 4.6 6.6a9 9 0 0 0 4.8 4.8L11 10l3.5 2-1 2.5C8 15 1 8 1.5 2.5Z" fill="var(--brand-blue-text)"/></svg>
          <span>+330 2718 4093</span>
        </li>
        <li class="contact-item">
          <svg class="contact-icon" viewBox="0 0 16 16" aria-hidden="true"><rect x="1" y="3" width="14" height="10" rx="1" fill="none" stroke="var(--brand-blue-text)" stroke-width="1.5"/><path d="M1.5 3.8 8 9l6.5-5.2" fill="none" stroke="var(--brand-blue-text)" stroke-width="1.5"/></svg>
          <span>info@halbrook.com</span>
        </li>
        <li class="contact-item">
          <svg class="contact-icon" viewBox="0 0 16 16" aria-hidden="true"><circle cx="8" cy="8" r="7" fill="var(--brand-blue-text)"/><path d="M1 8h14M8 1c-3 3-3 11 0 14M8 1c3 3 3 11 0 14" fill="none" stroke="#fff" stroke-width="1"/></svg>
          <span>www.halbrook.com</span>
        </li>
      </ul>
    </div>
  </section>

  <section class="card card-back">
    <span class="company-name">Halbrook Computer Group</span>
  </section>
</body>
</html>
```